Design Direction Exploration for Brand Deliverables

Here is the link to the finalized logo. If you have a design in this project, please use this version of the logo.

https://files.quorvane.net/get/QmRtPzKdYw

Here's the new web address: tidalharpnarrators.com

I need a business card, a Netlace Business Banner, a set of slides ("Opening Title slide and the "Thank You" slide), and two social media posts created in accordance with the current brand guidelines for "TidalHarp Narrators | For the Rivers Field". These deliverables should be made within Pintora so I can use them.

Target Market(s)

Professionals in the water sector. TidalHarp is a curated platform that connects water-focused organizations—NGOs, environmental firms, public utilities, and innovators—with exceptional voice actors. Our aim is to elevate the use of voice in storytelling across the water sector, from documentaries and e-learning to product launches and advocacy campaigns. This model puts voice actors first while also responding to a sector with growing communication needs.

Industry/Entity Type

TidalHarp Narrators | For the Rivers Field is the go-to authority in voice talent for the global water industry. Unlike traditional agencies, TidalHarp operates as a highly curated platform, connecting water and environment-focused firms, organizations, innovators, and advocates with exceptional human voice actors who bring clarity, credibility, and impact to their communication. From documentaries and promos to e-learning and product launches, our talent delivers performances at industry rates that engage audiences and elevate the stories shaping the future of water. By focusing exclusively on the water sector, TidalHarp ensures every client gains not only access to world-class voice actors but also a partner who understands the urgency and importance of their mission.

Font styles to use
Other font styles liked:
• See brand guidelines.

Colors

Designer to choose colors to be used in the design.

Requirements
Must have
• The elements of the three page brand guidelines: typeface, color palette, secondary element, and recommendation on photo usage.
Nice to have
• Use the three-page brand guidelines to influence your work. The products should feel high-end, inspirational, modern. If it were a home, it would be featured in Dwelling Quarterly. If it were a specific look, it would be featured in Flair. It's the Valtrane of voice talent. Luxurious, trustworthy, the go-to authority. I like some dimensionality/watermarks.
Should not have
• Cheap looking anything. The brand guidelines is a placeholder that I put together. I will update it based on what design this project yields.

```html
<!DOCTYPE html>
<html lang="en">
<head>
<meta charset="utf-8">
<title>TidalHarp Narrators – Slides and Netlace Banner</title>
<link href="https://fonts.googleapis.com/css2?family=Poppins:wght@300;400;500;600;700;800&display=swap" rel="stylesheet">
<style>
  :root{
    --page:#ececec;
    --navy:#0b2a4a;
    --navy-deep:#061d36;
    --blue:#0f5aa8;
    --blue-mid:#1f7fd0;
    --sky:#5cb6ee;
    --ice:#a9dcfa;
    --green:#7cc242;
    --white:#ffffff;
    --ink:#1b1b1b;
  }
  *{margin:0;padding:0;box-sizing:border-box}
  html,body{width:843px;height:1200px;overflow:hidden}
  body{background:var(--page);font-family:"Poppins",sans-serif;color:var(--white);position:relative}

  .slide{position:absolute;left:101px;width:641px;height:392px;overflow:hidden;border-radius:4px}
  .slide svg.waves{position:absolute;left:0;bottom:0;width:100%}

  /* Title slide */
  .title-slide{top:56px;background:linear-gradient(180deg,var(--blue-mid),var(--blue))}
  .title-slide .panel{position:absolute;left:18px;top:18px;right:18px;bottom:40px;border-radius:16px;
    border:2px solid rgba(169,220,250,.55);overflow:hidden;
    background:linear-gradient(180deg,rgba(6,29,54,.92),rgba(11,42,74,.8) 60%,rgba(15,90,168,.55))}
  .title-slide .water{position:absolute;inset:0;background:radial-gradient(ellipse at 50% 90%,rgba(92,182,238,.35),transparent 60%),linear-gradient(180deg,rgba(10,40,70,0),rgba(40,90,130,.4))}
  .title-slide .content{position:absolute;inset:0;display:flex;flex-direction:column;align-items:center;text-align:center;padding-top:40px}
  .brand{display:flex;align-items:center;gap:10px}
  .brand .dot{width:22px;height:22px;border-radius:50%;background:var(--white)}
  .brand .name{font-weight:700;font-size:28px;letter-spacing:.5px;color:var(--white)}
  .title-slide h1{margin-top:68px;font-weight:800;font-size:27px;letter-spacing:.3px;line-height:1.1}
  .title-slide h2{font-weight:600;font-size:26px;line-height:1.3}
  .date-pill{margin-top:16px;background:var(--green);color:var(--white);font-size:8px;font-weight:600;
    padding:4px 14px;border-radius:10px;letter-spacing:.4px}

  /* Thank you slide */
  .thanks-slide{top:500px;background:linear-gradient(180deg,var(--navy-deep),var(--navy))}
  .thanks-slide .panel{position:absolute;left:22px;top:22px;right:22px;bottom:22px;border-radius:16px;
    border:1.5px solid rgba(169,220,250,.35);background:linear-gradient(180deg,rgba(15,90,168,.25),rgba(15,90,168,.1))}
  .thanks-slide .left{position:absolute;left:60px;top:110px;width:220px}
  .social{display:flex;gap:8px;margin-top:40px;margin-left:30px}
  .social span{width:20px;height:20px;border-radius:50%;border:1.5px solid var(--white)}
  .thanks-slide .right{position:absolute;left:330px;top:104px}
  .thanks-slide h3{font-size:34px;font-weight:800;letter-spacing:.5px;line-height:1}
  .thanks-slide h3 .light{font-weight:400}
  .contacts{list-style:none;margin-top:22px}
  .contacts li{display:flex;align-items:center;gap:10px;font-size:8px;font-weight:400;line-height:1.35;margin-bottom:16px;color:#dfeaf5}
  .contacts .icon{flex:none;width:18px;height:18px;border-radius:50%;background:rgba(255,255,255,.18);display:flex;align-items:center;justify-content:center}
  .contacts .icon.green{background:var(--green)}

  /* Netlace banner */
  .section-label{position:absolute;left:101px;top:926px;font-size:15px;font-weight:700;color:var(--ink)}
  .banner{position:absolute;left:101px;top:972px;width:641px;height:165px;overflow:hidden;
    background:linear-gradient(180deg,var(--navy),var(--blue))}
  .banner .brand{position:absolute;left:44px;top:54px}
  .banner .brand .name{font-size:24px}
  .banner .tagline{position:absolute;left:330px;top:48px;text-align:center;width:210px}
  .banner .tagline strong{display:block;font-weight:700;font-size:15px}
  .banner .tagline span{display:block;font-weight:500;font-size:15px}
  .banner svg{position:absolute;left:0;bottom:0;width:100%}
</style>
</head>
<body>

<section class="slide title-slide">
  <svg class="waves" viewBox="0 0 641 140" preserveAspectRatio="none" height="140">
    <path d="M0 60 C120 20 220 90 340 55 S540 30 641 60 V140 H0Z" fill="#5cb6ee" opacity=".6"/>
    <path d="M0 85 C140 55 260 115 380 80 S560 70 641 90 V140 H0Z" fill="#a9dcfa" opacity=".7"/>
    <path d="M0 110 C150 90 280 130 420 105 S580 100 641 112 V140 H0Z" fill="#ffffff" opacity=".5"/>
  </svg>
  <div class="panel">
    <div class="water" role="img" aria-label="Dark ocean water surface photograph"></div>
    <div class="content">
      <div class="brand"><span class="dot"></span><span class="name">TidalHarp</span></div>
      <h1>TIDALHARP NARRATORS</h1>
      <h2>For the Rivers Field</h2>
      <div class="date-pill">SEPTEMBER 10,2025</div>
    </div>
  </div>
</section>

<section class="slide thanks-slide">
  <svg class="waves" viewBox="0 0 641 120" preserveAspectRatio="none" height="120">
    <path d="M0 50 C140 20 260 80 380 50 S560 30 641 55 V120 H0Z" fill="#1f7fd0" opacity=".18"/>
    <path d="M0 80 C150 60 290 105 420 78 S580 70 641 85 V120 H0Z" fill="#5cb6ee" opacity=".15"/>
  </svg>
  <div class="panel"></div>
  <div class="left">
    <div class="brand"><span class="dot"></span><span class="name">TidalHarp</span></div>
    <div class="social"><span></span><span></span><span></span></div>
  </div>
  <div class="right">
    <h3>THANK <span class="light">YOU</span></h3>
    <ul class="contacts">
      <li><span class="icon"><svg width="8" height="10" viewBox="0 0 8 10"><path d="M4 0a3.5 3.5 0 0 0-3.5 3.5C.5 6 4 10 4 10s3.5-4 3.5-6.5A3.5 3.5 0 0 0 4 0Zm0 5a1.4 1.4 0 1 1 0-2.8A1.4 1.4 0 0 1 4 5Z" fill="#fff"/></svg></span>1223,sed ut perspiciatis<br>unde omnis iste</li>
      <li><span class="icon green"><svg width="9" height="9" viewBox="0 0 10 10"><path d="M2 0.5 3.6 2.8 2.7 4a6 6 0 0 0 3.3 3.3l1.2-.9L9.5 8 8.6 9.5C4 9.5.5 6 .5 1.4Z" fill="#fff"/></svg></span>+1 888 888 8888</li>
      <li><span class="icon"><svg width="9" height="7" viewBox="0 0 10 7"><rect x=".5" y=".5" width="9" height="6" rx="1" fill="none" stroke="#fff"/><path d="M.5 1 5 4l4.5-3" fill="none" stroke="#fff"/></svg></span>info@companyname.ph</li>
    </ul>
  </div>
</section>

<div class="section-label">Netlace</div>

<section class="banner">
  <svg viewBox="0 0 641 165" preserveAspectRatio="none" height="165">
    <path d="M0 40 C120 10 230 70 350 40 S540 10 641 45 V165 H0Z" fill="#1f7fd0" opacity=".45"/>
    <path d="M0 90 C140 60 270 120 400 90 S570 70 641 95 V165 H0Z" fill="#5cb6ee" opacity=".55"/>
    <path d="M0 125 C150 105 290 150 430 125 S590 115 641 128 V165 H0Z" fill="#a9dcfa" opacity=".7"/>
    <path d="M0 145 C160 130 300 162 450 143 S600 138 641 146 V165 H0Z" fill="#7cc242"/>
  </svg>
  <div class="brand"><span class="dot"></span><span class="name">TidalHarp</span></div>
  <div class="tagline"><strong>TIDALHARP NARRATORS</strong><span>For the Rivers Field</span></div>
</section>

</body>
</html>
```